Wordpress Web Design & Coding for velnoragroup.ca

We need a website for a new investment company that is visually grabbing and vibrant. We would like to see a web page that displays trust, growth and confidence. Needs to be responsive and mobile friendly for all browsers and coded for both Android & IOS.

Open to the number of pages and menu items. I selected 4 but if you feel the layout would work better with less I am open to this. Need to sell the people (management team/related businesses) and then show where the invested money will be going (upcoming projects).

Company Info:

Velnora is an investment company put together by a group of seasoned business professionals who have come together to combine decades of success in the real estate development, management, financing and medical services. The company will be a full service company offering turn key solutions for medical professionals.

Vel-Nora will focus on providing a full range of services via a group of distinct companies to deliver newly emerging needs of the medical community. The end goal will be to create complete solutions for individuals in the medical community. Our group has experience and success with the conceptualization, construction and financing of medical and dental clinic spaces. Vel-Nora Group will be established to accommodate all areas of the development and creation of clinics for medical professionals from building construction to equipment financing and administrations.

You can mention these companies and take photos from their websites. You can also use stock photos.

Our construction partner:
https://382bld.com/projects/

Our equipment leasing partner:
https://www.pordiva.com/

Our Management Team and medical partners

Gil Parkes
https://www.mysoundpoise.ca/

Milos Vendraker
https://www.qrtdentalservices.com/about-us

PROPOSED PROJECTS (see attachment for details)
Hollowmere Business Park
Cresfield Business Park
Mt. Corwin Ridge Professional

Investors

Investment

Sans Serif

Must have
• Wordpress – must be both desktop and mobile friendly with fast page load speed
Ability to edit after ourselves in Wordpress
Attractive home page with logo etc.
Logo colours are: for the blue the pantone color is #0355a3
and for the green is #8cc63f

Sections, about us, what we do/services we provide, contact us

```html
<!DOCTYPE html>
<html lang="en">
<head>
<meta charset="utf-8">
<title>Vel-Nora Group</title>
<link href="https://fonts.googleapis.com/css2?family=Rubik:wght@400;500&family=Poppins:wght@300;400;500&display=swap" rel="stylesheet">
<style>
:root{
  --blue:#0355a3;
  --green:#8cc63f;
  --navy:#1d4a6e;
  --ink:#1f2b3a;
  --muted:#8a96a3;
  --soft:#f6f7f9;
  --field:#dde3e8;
  --white:#ffffff;
}
*{margin:0;padding:0;box-sizing:border-box}
html,body{width:1200px;height:3150px;overflow:hidden;background:var(--white)}
body{position:relative;font-family:"Poppins",sans-serif;color:var(--ink)}
.abs{position:absolute}
.heading{font-family:"Rubik",sans-serif}

/* header */
.site-header{position:absolute;left:0;top:0;width:1200px;height:95px;background:var(--white)}
.brand{position:absolute;left:78px;top:34px;display:flex;align-items:center;gap:8px;font-family:"Rubik",sans-serif;font-weight:500;font-size:19px;color:var(--blue)}
.brand-square{width:14px;height:14px;background:var(--green)}
.nav a{position:absolute;top:41px;font-family:"Rubik",sans-serif;font-size:13px;color:var(--ink);text-decoration:none;transform:translateX(-50%)}
.nav a.active{color:var(--green);border-bottom:1px solid var(--green)}
.call{position:absolute;left:982px;top:39px;font-family:"Rubik",sans-serif;font-size:15px;color:var(--blue)}

/* hero */
.hero{position:absolute;left:0;top:95px;width:1200px;height:465px;background:linear-gradient(110deg,#5d7894 0%,#9eb3c6 45%,#c7d3de 70%,#8ea4b8 100%)}
.hero h1{position:absolute;left:155px;top:113px;width:560px;font-family:"Rubik",sans-serif;font-weight:400;font-size:28px;line-height:34.5px;color:var(--white)}
.hero h1 b{font-weight:500}
.btn{position:absolute;display:flex;align-items:center;justify-content:center;border-radius:20px;font-family:"Poppins",sans-serif;font-weight:500;font-size:10px;letter-spacing:.5px;color:var(--white);text-transform:uppercase}
.btn-blue{background:var(--blue)}
.btn-green{background:var(--green)}
.dots{position:absolute;left:1032px;top:203px;display:flex;flex-direction:column;gap:6px}
.dots span{width:10px;height:10px;border:1px solid var(--white);border-radius:50%}
.dots span.on{background:radial-gradient(circle,var(--white) 2px,transparent 3px)}

/* about */
.about-art{position:absolute;left:155px;top:640px;width:399px;height:373px;background:linear-gradient(135deg,#2f6fc0 0%,#4c86cc 50%,#8cc63f 100%)}
.section-title{font-family:"Rubik",sans-serif;font-weight:400;font-size:27px;color:var(--blue);display:flex;align-items:center;gap:16px}
.rule{display:inline-block;width:48px;height:1px;background:var(--green)}
.about-title{position:absolute;left:612px;top:670px}
.about-copy{position:absolute;left:612px;top:719px;width:420px;font-size:12.5px;font-weight:300;line-height:19.2px;color:var(--muted)}
.about-copy p{margin-bottom:19px}
.about-copy em{font-style:normal;color:var(--blue)}

/* services */
.services{position:absolute;left:0;top:1092px;width:1200px;height:482px;background:var(--navy)}
.mark{position:absolute;width:16px;height:16px;border-radius:50%;background:var(--green);left:592px}
.centered-title{position:absolute;left:0;width:1200px;justify-content:center}
.service{position:absolute;top:185px;width:190px;text-align:center;transform:translateX(-50%)}
.service-icon{width:80px;height:80px;margin:0 auto;border-radius:50%;background:var(--white);display:flex;align-items:center;justify-content:center}
.service-icon.lit{background:var(--green)}
.service h3{margin-top:28px;font-family:"Rubik",sans-serif;font-weight:500;font-size:15px;color:var(--green)}
.service p{margin-top:10px;font-size:12.5px;font-weight:300;line-height:18px;color:#9fb2c4}
.read{margin-top:12px;font-size:10.5px;font-weight:500;letter-spacing:.8px;color:#9fb2c4}
.read.lit{color:var(--green)}

/* projects */
.card{position:absolute;top:1759px;width:280px;height:240px}
.card-img{height:161px}
.card-body{position:absolute;left:0;top:161px;width:240px;padding:18px 24px;border-top:2px solid var(--green);background:var(--white)}
.card-tab{position:absolute;right:0;top:161px;width:40px;height:38px;background:#3c4f63}
.card h3{font-family:"Rubik",sans-serif;font-weight:500;font-size:15px;color:var(--ink)}
.card h3.lit{color:var(--green)}
.card p{margin-top:6px;font-size:12.5px;font-weight:300;line-height:18px;color:var(--muted)}
.card p.link{text-decoration:underline}

/* partners */
.partners{position:absolute;left:0;top:2079px;width:1200px;height:177px;background:var(--soft)}
.partners h2{position:absolute;left:0;top:38px;width:1185px;text-align:center;font-family:"Rubik",sans-serif;font-weight:400;font-size:15px;color:var(--blue)}
.partner{position:absolute;top:90px;transform:translateX(-50%);font-family:"Rubik",sans-serif;font-size:22px;color:#4a4f55}

/* team */
.member{position:absolute;top:2440px;width:220px;text-align:center;transform:translateX(-50%)}
.avatar{width:159px;height:159px;margin:0 auto;border-radius:50%;background:radial-gradient(circle at 50% 40%,#d8d2cc 0%,#b9b3ae 60%,#8c8782 100%)}
.member h3{margin-top:16px;font-family:"Rubik",sans-serif;font-weight:500;font-size:14.5px;color:var(--ink)}
.member p{margin-top:4px;font-size:12.5px;font-weight:300;color:var(--muted)}

/* footer */
.site-footer{position:absolute;left:0;top:2725px;width:1200px;height:425px;background:#f4f7f9}
.footer-brand{position:absolute;left:155px;top:118px;display:flex;align-items:center;gap:8px;font-family:"Rubik",sans-serif;font-weight:500;font-size:22px;color:var(--blue)}
.contact{position:absolute;left:360px;top:90px;font-size:14px;color:var(--ink)}
.contact h2{font-family:"Rubik",sans-serif;font-weight:500;font-size:18px;margin-bottom:16px}
.contact .call-line{font-size:16px}
.contact .call-line span{color:var(--blue)}
.contact .mail{font-size:13px;margin-top:2px}
.contact .org{margin-top:22px;font-size:13px;color:var(--blue)}
.contact .org span{color:var(--green)}
.contact .addr{font-size:13px;line-height:20px}
.social{position:absolute;top:277px;width:32px;height:32px;border-radius:50%;background:var(--blue)}
.social.lit{background:var(--green)}
.field{position:absolute;height:31px;border-radius:16px;background:var(--field);padding:9px 16px;font-size:11.5px;color:#4d5864}
.copyright{position:absolute;left:0;top:360px;width:1185px;text-align:center;font-size:12px;color:var(--ink)}
.copyright span{color:var(--blue)}
.copyright i{font-style:normal;color:var(--green)}
</style>
</head>
<body>

<header class="site-header">
  <div class="brand"><span class="brand-square"></span>Vel-Nora Group</div>
  <nav class="nav">
    <a class="active" style="left:355px">Home</a>
    <a style="left:440px">About Us</a>
    <a style="left:531px">Services</a>
    <a style="left:620px">Partners</a>
    <a style="left:707px">Projects</a>
    <a style="left:785px">Team</a>
    <a style="left:880px">Contact Us</a>
  </nav>
  <div class="call">Call: 44-510-0192</div>
</header>

<section class="hero">
  <div class="abs" role="img" aria-label="Business team reviewing financial charts at a meeting table" style="inset:0"></div>
  <h1><b>VEL-NORA</b> will focus on providing a full range of services via a group of distinct companies to deliver newly emerging needs of the medical community.</h1>
  <div class="btn btn-blue" style="left:155px;top:317px;width:129px;height:32px">Contact Us</div>
  <div class="dots"><span></span><span></span><span class="on"></span><span></span></div>
</section>

<section class="about">
  <div class="about-art" role="img" aria-label="Handshake photo framed in blue and green brand shapes"></div>
  <h2 class="section-title about-title">About Us <span class="rule"></span></h2>
  <div class="about-copy">
    <p><em>Vel-Nora</em> is an investment company put together by a group of seasoned business professionals who have come together to combine decades of success in the real estate development, management, financing and medical services. The company will be a full service company offering turn key solutions for medical professionals.</p>
    <p><em>Vel-Nora</em> will focus on providing a full range of services via a group of distinct companies to deliver newly emerging needs of the medical community ...</p>
  </div>
  <div class="btn btn-green" style="left:612px;top:945px;width:128px;height:33px">Discover More</div>
</section>

<section class="services">
  <span class="mark" style="top:86px"></span>
  <h2 class="section-title centered-title" style="top:118px"><span class="rule"></span>Services We Provide<span class="rule"></span></h2>
  <div class="service" style="left:258px">
    <div class="service-icon"><svg width="36" height="36" viewBox="0 0 36 36" fill="none" stroke="#8cc63f" stroke-width="1.6"><rect x="8" y="6" width="14" height="26"/><rect x="22" y="16" width="8" height="16"/><path d="M12 11h2M16 11h2M12 16h2M16 16h2M12 21h2M16 21h2M15 32v-5"/></svg></div>
    <h3>Real Estate Development</h3>
    <p>It is a long established fact that a reader will be distracted the readable ...</p>
    <div class="read">READ MORE &nbsp;›</div>
  </div>
  <div class="service" style="left:486px">
    <div class="service-icon lit"><svg width="38" height="38" viewBox="0 0 38 38" fill="none" stroke="#fff" stroke-width="1.6"><circle cx="19" cy="16" r="9"/><circle cx="19" cy="16" r="3.5"/><path d="M14 25v6h10v-6"/></svg></div>
    <h3>Management</h3>
    <p>It is a long established fact that a reader will be distracted the readable ...</p>
    <div class="read lit">READ MORE &nbsp;›</div>
  </div>
  <div class="service" style="left:713px">
    <div class="service-icon"><svg width="38" height="38" viewBox="0 0 38 38" fill="none" stroke="#8cc63f" stroke-width="1.6"><circle cx="20" cy="13" r="6"/><path d="M6 26h8l6 3 10-5M6 30h6l8 3 12-7"/></svg></div>
    <h3>Financing</h3>
    <p>It is a long established fact that a reader will be distracted the readable ...</p>
    <div class="read">READ MORE &nbsp;›</div>
  </div>
  <div class="service" style="left:942px">
    <div class="service-icon"><svg width="38" height="38" viewBox="0 0 38 38" fill="none" stroke="#8cc63f" stroke-width="1.6"><path d="M10 6v10a6 6 0 0 0 12 0V6"/><path d="M16 22v5a6 6 0 0 0 12 0v-5"/><circle cx="28" cy="19" r="3"/></svg></div>
    <h3>Medical Services</h3>
    <p>It is a long established fact that a reader will be distracted the readable ...</p>
    <div class="read">READ MORE &nbsp;›</div>
  </div>
</section>

<section class="projects">
  <span class="mark" style="top:1661px"></span>
  <h2 class="section-title centered-title" style="top:1694px"><span class="rule"></span>Our Projects<span class="rule"></span></h2>
  <article class="card" style="left:155px">
    <div class="card-img" role="img" aria-label="Glass office tower seen from below" style="background:linear-gradient(135deg,#c9dbea,#7e9fbd 60%,#4b6a88)"></div>
    <div class="card-tab"></div>
    <div class="card-body"><h3>Hollowmere Business Park</h3><p>Office &amp; Light Industrial Building Projects</p></div>
  </article>
  <article class="card" style="left:460px">
    <div class="card-img" role="img" aria-label="Modern office building beside green trees" style="background:linear-gradient(135deg,#b9d1e6,#6f8ea8 55%,#5d8a3e)"></div>
    <div class="card-tab" style="background:#6d7c5e"></div>
    <div class="card-body"><h3 class="lit">Cresfield Business Park</h3><p class="link">Core Municipality in the Western Communities</p></div>
  </article>
  <article class="card" style="left:763px">
    <div class="card-img" role="img" aria-label="Low-rise professional office building with glass bands" style="background:linear-gradient(135deg,#d8e4ee,#a8b8c6 60%,#7d8f9f)"></div>
    <div class="card-tab" style="background:#8a98a6"></div>
    <div class="card-body"><h3>Mt. Corwin Ridge Professional</h3><p>Professional Services Building</p></div>
  </article>
</section>

<section class="partners">
  <h2>Our Partners</h2>
  <div class="partner" style="left:301px">382 Builders</div>
  <div class="partner" style="left:504px">Pordiva</div>
  <div class="partner" style="left:707px">soundpoise</div>
  <div class="partner" style="left:903px">QRT Dental</div>
</section>

<section class="team">
  <span class="mark" style="top:2341px"></span>
  <h2 class="section-title centered-title" style="top:2375px"><span class="rule"></span>Experienced Team<span class="rule"></span></h2>
  <div class="member" style="left:336px"><div class="avatar" role="img" aria-label="Portrait photo of Teo Marchand"></div><h3>Teo Marchand</h3><p>Contrary to popular</p></div>
  <div class="member" style="left:599px"><div class="avatar" role="img" aria-label="Portrait photo of Milos Vendraker"></div><h3>Milos Vendraker</h3><p>Lorem Ipsum</p></div>
  <div class="member" style="left:863px"><div class="avatar" role="img" aria-label="Portrait photo of Dr. Gil Parkes"></div><h3>Dr. Gil Parkes</h3><p>Lorem Ipsum</p></div>
</section>

<footer class="site-footer">
  <div class="footer-brand"><span class="brand-square"></span>Vel-Nora Group</div>
  <div class="contact">
    <h2>Contact Us</h2>
    <div class="call-line">Call Us: <span>(44)-510-0192</span></div>
    <div class="mail">e. info@velnoragroup.ca</div>
    <div class="org">Vel-Nora <span>Group</span></div>
    <div class="addr">4410 Alder Crest Way<br>Brenton, NR 60418</div>
  </div>
  <span class="social" style="left:359px" aria-label="Social link"></span>
  <span class="social lit" style="left:399px" aria-label="Social link"></span>
  <span class="social" style="left:438px" aria-label="Social link"></span>
  <div class="field" style="left:612px;top:85px;width:206px">Name</div>
  <div class="field" style="left:835px;top:85px;width:208px">Email</div>
  <div class="field" style="left:612px;top:134px;width:431px">Subject</div>
  <div class="field" style="left:612px;top:182px;width:431px;height:78px;border-radius:14px">Message ...</div>
  <div class="btn btn-blue" style="left:612px;top:277px;width:96px;height:32px;font-size:12px;text-transform:none;font-weight:400">Send</div>
  <svg class="abs" style="left:1122px;top:96px" width="24" height="26" viewBox="0 0 24 26" fill="none" stroke="#0355a3" stroke-width="2"><path d="M2 24L12 2l10 22-10-6z"/></svg>
  <div class="copyright">© 2020 <span>Vel-Nora</span> <i>Group.</i> All Right Reserved</div>
</footer>

</body>
</html>
```